Gearhead Rally 5, The fifth annual Gearhead Rally motorcycle event, www.gearheadrally.example

We need an event poster that can be used in print and on the web to promote our event. Files for the poster should be modifiable to add additional information as it becomes available. The Gearhead Rally is a gathering for Vintage, Classic and Cafe' Racer motorcycles and their riders, Rockers and Mods. The event date is Saturday, July 26, 2014, rain or shine, from 9:00 AM to 6:00 PM EDT at Havelock Green, 217 Birchmont Avenue, Pittston, PA 18917 USA. Friday July 25 Meet and Greet from 7:00 PM to close at Mallory's Lagoon, Pittston, PA. Survivors' Breakfast, Sunday, July 27, 7:00 to 10:00 AM, location tba. Optional Group Ride Saturday from 10:00 AM to Noon. Vexlor 450 Custom Cafe' Motorcycle Raffle, Contests, Trophies and Cash Prizes for Pin-up Girl, Coolest Cafe' Racer Motorcycle, Coolest Mod Scooter, Peoples Choice Motorcycle, and More! Live music by the one and only legendary TLWZ, "Slim Uncle" Rook and more tba. Brought to you by Ridgeline Throttlers, www.social.example/ridgelinethrottlers?ref=hl, Quimby and Holt/Holt Rascals, www.quimbyandholt.example. Partial Proceeds to benefit the BWVRL and The Lower Valley Rescue Squad Society. More information and advance tickets available at www.gearheadrally.example

Thank you to all who participated in our competition.  We received excellent work from you all, and the hard part for us is having to choose.  Our decision will be made today.

```html
<!DOCTYPE html>
<html lang="en">
<head>
<meta charset="utf-8">
<title>Gearhead Rally 5 – Event Poster</title>
<link rel="stylesheet" href="https://fonts.googleapis.com/css2?family=Montserrat:wght@500;600;700&family=Share+Tech+Mono&display=swap">
<style>
  :root {
    --stage-top: #6f6f6f;
    --stage-bottom: #c9c9c9;
    --rally-red: #c8232c;
    --rally-red-dark: #8f1219;
    --navy: #2b2d6b;
    --navy-text: #3a40a8;
    --ink: #0b0b0b;
    --night: #141414;
    --white: #ffffff;
    --chrome-light: #bdbdbd;
    --chrome-dark: #3a3a3a;
    --head: "Montserrat", Arial, sans-serif;
    --mono: "Share Tech Mono", "Courier New", monospace;
  }
  * { box-sizing: border-box; margin: 0; padding: 0; }
  html, body { width: 1200px; height: 1000px; overflow: hidden; }
  body { background: linear-gradient(180deg, var(--stage-top), var(--stage-bottom)); position: relative; }

  .poster { position: absolute; left: 266px; top: 0; width: 666px; height: 1000px; background: var(--night); overflow: hidden; }

  .hero { position: absolute; left: 0; top: 0; width: 666px; height: 525px;
    background: radial-gradient(ellipse at 40% 35%, var(--rally-red) 0%, #b81d25 60%, var(--rally-red-dark) 100%); }
  .hero svg { position: absolute; inset: 0; }
  .kicker { font-family: var(--head); font-weight: 600; fill: var(--ink); }
  .title { font-family: var(--head); font-weight: 500; fill: var(--white); }
  .tagline { font-family: var(--mono); font-size: 21px; fill: var(--white); letter-spacing: 1px; }
  .event-date { font-family: var(--head); font-weight: 600; font-size: 40px; fill: var(--white); }

  .info-strip { position: absolute; left: 0; top: 525px; width: 666px; height: 30px; background: var(--ink);
    color: var(--white); font-family: var(--mono); font-size: 10.5px; letter-spacing: .2px; white-space: nowrap;
    display: flex; align-items: center; justify-content: center; }

  .schedule { position: absolute; left: 0; top: 560px; width: 666px; height: 180px; }
  .slot { position: absolute; width: 205px; transform: rotate(-8deg); text-align: center; }
  .slot-flag { display: flex; align-items: center; justify-content: center; height: 74px;
    font-family: var(--head); font-weight: 600; font-size: 25px; line-height: 1; color: var(--white); letter-spacing: -.5px; }
  .slot-flag.red { background: var(--rally-red); }
  .slot-flag.navy { background: var(--navy); }
  .slot-details { margin-top: 10px; font-family: var(--mono); font-size: 18px; line-height: 1.25; color: var(--white); }
  .slot.meet { left: 14px; top: 14px; }
  .slot.breakfast { left: 232px; top: 6px; }
  .slot.ride { left: 448px; top: 0; }

  .raffle { position: absolute; left: 0; top: 742px; width: 666px; text-align: center; }
  .raffle h2 { font-family: var(--head); font-weight: 600; font-size: 24px; color: var(--white); letter-spacing: -.2px; white-space: nowrap; }
  .raffle p { margin-top: 6px; font-family: var(--mono); font-size: 13.5px; line-height: 1.35; color: var(--navy-text); letter-spacing: .4px; }

  .lineup { position: absolute; left: 15px; top: 830px; width: 635px; height: 66px; border: 2px solid var(--rally-red);
    display: flex; align-items: center; justify-content: center; text-align: center;
    font-family: var(--head); font-weight: 600; font-size: 18px; line-height: 1.3; color: var(--white); }

  .credits { position: absolute; left: 0; top: 910px; width: 666px; height: 90px; background: var(--white); color: var(--ink); }
  .credits-label { position: absolute; left: 12px; top: 10px; font-family: var(--head); font-weight: 700; font-size: 9.5px; }
  .sponsor { position: absolute; top: 32px; display: flex; align-items: center; gap: 7px; }
  .sponsor.throttlers { left: 14px; }
  .sponsor.rascals { left: 196px; }
  .sponsor-dot { width: 44px; height: 44px; border-radius: 50%; background: var(--ink); flex: none; }
  .sponsor-name { font-family: var(--head); font-weight: 600; font-size: 11px; line-height: 1.15; white-space: nowrap; }
  .sponsor-url { display: block; font-family: var(--head); font-weight: 600; font-size: 5.5px; margin-top: 2px; }
  .benefit { position: absolute; right: 14px; top: 16px; width: 290px; text-align: center;
    font-family: var(--head); font-weight: 600; font-size: 10.5px; line-height: 1.3; }
  .benefit strong { font-weight: 700; }
</style>
</head>
<body>
<main class="poster">
  <section class="hero">
    <svg width="666" height="525" viewBox="0 0 666 525" xmlns="http://www.w3.org/2000/svg">
      <text class="kicker" x="14" y="62" font-size="62" textLength="638" lengthAdjust="spacingAndGlyphs">THE FIFTH ANNUAL</text>
      <text class="title" x="12" y="182" font-size="134" textLength="642" lengthAdjust="spacingAndGlyphs">GEARHEAD</text>
      <text class="title" x="16" y="394" font-size="270" textLength="638" lengthAdjust="spacingAndGlyphs">RALLY</text>
      <polygon points="6,324 666,200 666,232 12,356" fill="var(--navy)"/>
      <text class="tagline" transform="translate(18 349) rotate(-10.6)" textLength="620" lengthAdjust="spacingAndGlyphs">VINTAGE, CLASSIC AND CAFÉ RACER MOTORCYCLES AND THEIR RIDERS</text>
      <defs>
        <linearGradient id="chrome" x1="0" y1="0" x2="0" y2="1">
          <stop offset="0" stop-color="var(--chrome-light)"/>
          <stop offset="1" stop-color="var(--chrome-dark)"/>
        </linearGradient>
      </defs>
      <rect role="img" aria-label="Halftone photo of a silver café racer motorcycle" x="28" y="338" width="600" height="187" rx="40" fill="url(#chrome)" opacity="0.9"/>
      <text class="event-date" x="652" y="436" text-anchor="end" textLength="262" lengthAdjust="spacingAndGlyphs">JULY 26 2014</text>
    </svg>
  </section>

  <div class="info-strip">RAIN OR SHINE. 09:00 AM TO 06:00 PM EDT AT HAVELOCK GREEN, 217 BIRCHMONT AVENUE, PITTSTON, PA 18917 USA</div>

  <section class="schedule">
    <div class="slot meet">
      <div class="slot-flag red">MEET AND<br>GREET</div>
      <div class="slot-details">Friday, July 25<br>07:00 PM To Close<br>Mallory’s Lagoon</div>
    </div>
    <div class="slot breakfast">
      <div class="slot-flag navy">SURVIVORS’<br>BREAKFAST</div>
      <div class="slot-details">Sunday, July 27<br>07:00 AM To 10:00 AM<br>Location Tba</div>
    </div>
    <div class="slot ride">
      <div class="slot-flag red">OPTIONAL<br>GROUP RIDE</div>
      <div class="slot-details">Saturday, July 26<br>10:00 AM To Noon</div>
    </div>
  </section>

  <section class="raffle">
    <h2>VEXLOR 450 CUSTOM CAFE’ MOTORCYCLE RAFFLE</h2>
    <p>CONTESTS, TROPHIES AND CASH PRIZES FOR PIN-UP GIRL, COOLEST CAFE’ RACER MOTORCYCLE,<br>COOLEST MOD SCOOTER, PEOPLES CHOICE MOTORCYCLE, AND MORE!</p>
  </section>

  <section class="lineup">
    <p>LIVE MUSIC BY THE ONE AND ONLY LEGENDARY TLWZ,<br>“SLIM UNCLE” ROOK AND MORE TBA.</p>
  </section>

  <footer class="credits">
    <div class="credits-label">BROUGHT TO YOU BY:</div>
    <div class="sponsor throttlers">
      <span class="sponsor-dot"></span>
      <span class="sponsor-name">Ridgeline Throttlers<span class="sponsor-url">www.social.example/ridgelinethrottlers</span></span>
    </div>
    <div class="sponsor rascals">
      <span class="sponsor-dot"></span>
      <span class="sponsor-name">Quimby and Holt/<br>Holt Rascals<span class="sponsor-url">www.quimbyandholt.example</span></span>
    </div>
    <p class="benefit">Partial Proceeds to benefit the BWVRL and<br>The Lower Valley Rescue Squad Society.<br>More information and advance tickets available at<br><strong>www.gearheadrally.example</strong></p>
  </footer>
</main>
</body>
</html>
```